Ferncrest Dental, LLC business card project

Business card to be designed with current logo.
Dental office- please keep design of card that looks clean and professional.
Please include the following info:
Ferncrest Dental, LLC
Dr. Lorna Pettigrew
2871 Marlowe Street
Bethlehem, PA 18093
610-555-0193
ferncrestdental.office@examplemail.test
Hello everyone-
Reason: Just got back from overseas- will look at all designs and provide feedback. Thank you!
Reason: Polling my friends for the final selection-
thank you to all those that participated- so many talented designers!

```html
<!DOCTYPE html>
<html lang="en">
<head>
<meta charset="utf-8">
<title>Ferncrest Dental, LLC — Business Card</title>
<link href="https://fonts.googleapis.com/css2?family=Arimo&family=Jost:wght@400;500&display=swap" rel="stylesheet">
<style>
  :root {
    --backdrop: #5f5f61;
    --card: #e6e7e9;
    --green-dark: #6a9f4b;
    --green-text: #6aa04a;
    --green-light: #c5dd6e;
    --green-pale: #f2f8e2;
    --logo-dot: #a9c94a;
  }
  * { margin: 0; padding: 0; box-sizing: border-box; }
  html, body {
    width: 981px;
    height: 1200px;
    overflow: hidden;
    background: var(--backdrop);
  }
  .sheet {
    position: relative;
    width: 981px;
    height: 1200px;
  }
  .card {
    position: absolute;
    left: 46px;
    width: 887px;
    height: 508px;
    background: var(--card);
    overflow: hidden;
  }
  .card--front { top: 56px; }
  .card--back { top: 635px; }

  .card__wave {
    position: absolute;
    inset: 0;
    width: 887px;
    height: 508px;
  }

  .brand {
    position: absolute;
    display: flex;
    align-items: center;
    gap: 14px;
    font-family: "Jost", sans-serif;
    font-weight: 400;
    font-size: 46px;
    color: var(--green-dark);
    white-space: nowrap;
    letter-spacing: -0.5px;
  }
  .brand__dot {
    width: 26px;
    height: 26px;
    border-radius: 50%;
    background: var(--logo-dot);
    flex: none;
  }
  .card--front .brand {
    right: 58px;
    top: 70px;
  }
  .card--back .brand {
    left: 50%;
    top: 50%;
    transform: translate(-50%, -50%);
  }

  .contact {
    position: absolute;
    left: 103px;
    top: 342px;
    font-family: "Arimo", sans-serif;
    font-size: 18.5px;
    line-height: 23.8px;
    color: var(--green-text);
    list-style: none;
  }

  .doctor {
    position: absolute;
    right: 59px;
    top: 400px;
    font-family: "Jost", sans-serif;
    font-weight: 500;
    font-size: 42px;
    letter-spacing: 1px;
    color: var(--green-dark);
    white-space: nowrap;
  }
</style>
</head>
<body>
<main class="sheet">
  <section class="card card--front">
    <svg class="card__wave" viewBox="0 0 1051 602" preserveAspectRatio="none" aria-hidden="true">
      <defs>
        <linearGradient id="meadow" x1="0" y1="0" x2="1" y2="0">
          <stop offset="0" stop-color="#c5dd6e"/>
          <stop offset="0.55" stop-color="#e0ecb0"/>
          <stop offset="1" stop-color="#f2f8e2"/>
        </linearGradient>
        <linearGradient id="ribbon" x1="0" y1="0" x2="1" y2="0">
          <stop offset="0" stop-color="#6a9f4b"/>
          <stop offset="0.18" stop-color="#7fae5c"/>
          <stop offset="0.3" stop-color="#6a9f4b"/>
          <stop offset="1" stop-color="#6a9f4b"/>
        </linearGradient>
      </defs>
      <path d="M0,128 C200,262 450,342 700,347 C820,350 950,340 1051,322 L1051,602 L0,602 Z" fill="url(#meadow)"/>
      <path d="M0,75 C200,205 450,300 700,312 C850,318 960,302 1051,284 L1051,322 C950,340 820,350 700,347 C450,342 200,262 0,128 Z" fill="url(#ribbon)"/>
    </svg>

    <div class="brand">
      <span class="brand__dot"></span>
      <span class="brand__name">Ferncrest Dental, LLC</span>
    </div>

    <ul class="contact">
      <li>2871 Marlowe Street</li>
      <li>Bethlehem, PA 18093</li>
      <li>610-555-0193</li>
      <li>ferncrestdental.office@examplemail.test</li>
    </ul>

    <p class="doctor">Dr. Lorna Pettigrew</p>
  </section>

  <section class="card card--back">
    <div class="brand">
      <span class="brand__dot"></span>
      <span class="brand__name">Ferncrest Dental, LLC</span>
    </div>
  </section>
</main>
</body>
</html>
```